Harbor Vantage Web Design Project

We need a website design for a start up company called "Harbor Vantage". We provide business consultancy services as well as technology-related services (IT). The design should communicate simplicity and elegance. The domain name of the site will be harborvantage-example.com. The logo of the company is https://files.example-share.net/u/7418205/4630_2116587_67315_image.jpg

Target Market(s)

SMB, Corporates, Semi-governments, Governments.

Industry/Entity Type

Business

Requirements
Must have
• - The background of the pages should be white or soft grey, but we are open for suggestions.
- The pages should have nice menu animations.
- The pages should be "portal-style", with multiple placeholders for different sections and multiple tabs.
Nice to have
• The page should auto-fit the screen and scroll vertically as much as needed.
Should not have
• - Flash Animations.
- Generic Photos.

```html
<!DOCTYPE html>
<html lang="en">
<head>
<meta charset="utf-8">
<title>Harbor Vantage</title>
<link rel="stylesheet" href="https://fonts.googleapis.com/css2?family=Oswald:wght@400;500&family=Montserrat:wght@600&family=Questrial&display=swap">
<style>
:root{
  --red:#d81f26;
  --red-dark:#b8161c;
  --blue:#1d5aa6;
  --blue-dark:#154a8c;
  --grey-text:#6d6d6d;
  --grey-light:#f2f2f2;
  --grey-mid:#d9d9d9;
  --white:#ffffff;
  --body:#4a4a4a;
}
*{margin:0;padding:0;box-sizing:border-box}
html,body{width:1200px;height:1065px;overflow:hidden}
body{
  position:relative;
  font-family:"Questrial",sans-serif;
  background:radial-gradient(ellipse at 50% 35%,#ffffff 0%,#f6f6f6 45%,#dedede 100%);
}
.abs{position:absolute}
.fit{display:inline-block;white-space:nowrap;transform-origin:left top}
.search{left:739px;top:22px;width:170px;height:17px;border:1px solid #d6d6d6;border-radius:9px;background:var(--white);font-size:9px;color:var(--grey-text);padding:3px 0 0 9px}
.search svg{position:absolute;right:6px;top:4px}
.brand{left:0;width:1200px;top:180px;text-align:center;font-family:"Questrial",sans-serif;font-size:24px;color:var(--blue)}
.brand-dot{display:inline-block;width:12px;height:12px;border-radius:50%;background:var(--red);margin-right:8px;vertical-align:2px}
.social{display:flex;gap:4px}
.social span{width:15px;height:15px;background:#c9c9c9;border-radius:2px}
.social.top{left:635px;top:227px}
.nav{left:528px;top:286px;display:flex;align-items:center;font-size:11.5px;color:var(--blue);letter-spacing:.2px}
.nav a{color:inherit;text-decoration:none}
.nav a.active{color:var(--red)}
.nav .sep{color:#c5c5c5;margin:0 14px;font-size:9px}
.hero-word{left:284px;top:325px;font-family:"Montserrat",sans-serif;font-weight:600;font-size:122px;letter-spacing:-4px;color:var(--red);line-height:1;text-shadow:0 2px 3px rgba(0,0,0,.15)}
.hero-word .fit{transform:scaleX(.78)}
.hero-tag{left:288px;top:437px;font-family:"Questrial",sans-serif;font-size:12.5px;color:var(--blue);letter-spacing:-.9px}
.hero-tag .fit{transform:scaleX(.93)}
.offer-band{left:0;top:470px;width:1200px;height:60px;background:var(--grey-light);border-top:1px solid #e2e2e2;border-bottom:1px solid #e2e2e2}
.offer-text{left:288px;top:485px;font-family:"Oswald",sans-serif;font-size:22px;color:var(--grey-text);letter-spacing:-1px}
.offer-text .fit{transform:scaleX(.73)}
.cta{left:700px;top:476px;width:204px;height:60px;background:repeating-linear-gradient(45deg,var(--blue) 0 2px,var(--blue-dark) 2px 4px);color:var(--white);font-family:"Oswald",sans-serif;font-size:28px;letter-spacing:-1.2px;line-height:60px;padding-left:13px;overflow:hidden}
.cta .fit{transform:scaleX(.8)}
.portal-fade{left:0;top:530px;width:1200px;height:113px;background:linear-gradient(#f2f2f2,#d6d6d6)}
.portal-band{left:0;top:643px;width:1200px;height:86px;background:linear-gradient(90deg,var(--red-dark),var(--red) 15%,var(--red) 85%,var(--red-dark))}
.portal{top:566px;width:190px;text-align:center}
.portal .art{width:110px;height:110px;margin:0 auto;border-radius:14px}
.portal h3{margin-top:16px;font-family:"Oswald",sans-serif;font-weight:400;font-size:21px;color:var(--white);letter-spacing:-.5px}
.divider{top:665px;width:1px;height:55px;border-left:1px dotted rgba(255,255,255,.5)}
.content{left:0;top:729px;width:1200px;height:237px;background:var(--white)}
.welcome{left:288px;top:762px;font-family:"Oswald",sans-serif;font-weight:500;font-size:44px;color:var(--blue);letter-spacing:-2.5px;line-height:1}
.welcome .fit{transform:scaleX(.9)}
.welcome-name{left:288px;top:808px;width:174px;text-align:right;font-size:16px;color:var(--red)}
.vline{left:485px;top:765px;width:1px;height:75px;background:#dcdcdc}
.lead{left:500px;top:765px;width:425px;font-size:16px;color:var(--blue);letter-spacing:-.8px;line-height:19px}
.lorem{left:500px;top:813px;width:412px;font-family:Arial,sans-serif;font-size:7.6px;color:var(--body);line-height:10px}
.hrule{left:286px;top:870px;width:626px;height:1px;background:#e4e4e4}
.grow{left:286px;top:890px;font-size:19px;color:var(--red);letter-spacing:-.6px}
.features{left:286px;top:928px;width:626px;display:flex;justify-content:space-between}
.features li{list-style:none;display:flex;align-items:center;gap:7px;font-family:Arial,sans-serif;font-size:7.8px;color:var(--red)}
.footer{left:0;top:966px;width:1200px;height:99px;background:radial-gradient(ellipse at 50% 0%,#f4f4f4,#dcdcdc)}
.foot-copy{left:325px;top:1009px;font-family:Arial,sans-serif;font-size:7.6px;color:var(--grey-text)}
.foot-line{left:292px;top:1031px;width:116px;height:1px;background:#9a9a9a}
.social.bottom{left:415px;top:1023px}
.news-title{left:553px;top:1001px;font-size:12.5px;color:#555}
.news-input{left:549px;top:1019px;width:180px;height:17px;border-radius:9px;background:var(--white);border:1px solid #ddd;overflow:hidden}
.news-input span{position:absolute;right:0;top:0;height:100%;width:47px;background:var(--red);color:var(--white);font-family:Arial,sans-serif;font-size:6.5px;line-height:16px;text-align:center}
.call-title{left:814px;top:1001px;font-size:13px;color:#555}
.call-icon{left:784px;top:1017px;width:22px;height:22px;border-radius:50%;background:#e6e6e6;border:1px solid #ccc}
.call-icon svg{position:absolute;left:5px;top:5px}
.phone{left:812px;top:1018px;font-family:"Oswald",sans-serif;font-size:17px;color:var(--red);letter-spacing:-.8px}
</style>
</head>
<body>
<div class="abs search">Enter Your Keywords Here..
  <svg width="7" height="7" viewBox="0 0 7 7"><circle cx="3" cy="3" r="2" fill="none" stroke="#777" stroke-width="1"/><line x1="4.5" y1="4.5" x2="6.5" y2="6.5" stroke="#777"/></svg>
</div>

<div class="abs brand"><span class="brand-dot"></span>Harbor Vantage</div>
<div class="abs social top"><span></span><span></span><span></span><span></span></div>

<nav class="abs nav">
  <a class="active" href="#">HOME</a><span class="sep">|</span>
  <a href="#">ABOUT US</a><span class="sep">|</span>
  <a href="#">SERVICES</a><span class="sep">|</span>
  <a href="#">SOLUTIONS</a><span class="sep">|</span>
  <a href="#">CONTACTS</a>
</nav>

<h1 class="abs hero-word"><span class="fit">DEVELOP</span></h1>
<p class="abs hero-tag"><span class="fit">B2B AND B2C SAAS BASED SOLUTIONS AND E-COMMERCE PORTALS FOR COMPANIES</span></p>

<div class="abs offer-band"></div>
<p class="abs offer-text"><span class="fit">ARE YOU INTERESTED IN OUR OFFER? DO YOU HAVE ANY QUESTIONS?</span></p>
<a class="abs cta"><span class="fit">GET IN TOUCH WITH US</span></a>

<div class="abs portal-fade"></div>
<div class="abs portal-band"></div>
<div class="abs portal" style="left:283px">
  <div class="art" role="img" aria-label="Illustration of a globe with a backpack" style="background:linear-gradient(135deg,#8a8a78,#3f7cc0 60%,#4a4a40)"></div>
  <h3>B2B PORTALS</h3>
</div>
<div class="abs divider" style="left:483px"></div>
<div class="abs portal" style="left:498px">
  <div class="art" role="img" aria-label="Illustration of two business people" style="background:linear-gradient(135deg,#3a3a3a,#e8b995 50%,#2f5ea8)"></div>
  <h3>B2C PORTALS</h3>
</div>
<div class="abs divider" style="left:691px"></div>
<div class="abs portal" style="left:711px">
  <div class="art" role="img" aria-label="Illustration of a paper shopping bag" style="background:linear-gradient(135deg,#e6e2cf,#c8c2a6 60%,#9a2a20)"></div>
  <h3>E-COMMERCE PORTALS</h3>
</div>

<div class="abs content"></div>
<h2 class="abs welcome"><span class="fit">WELCOME TO</span></h2>
<p class="abs welcome-name">Harbor Vantage</p>
<div class="abs vline"></div>
<p class="abs lead">We are proud to deliver immediate results through active skills, and real-world tasks ..</p>
<p class="abs lorem">Lorem ipsum dolor sit amet, consectetuer adipiscing elit, sed diam nonummy nibh euismod tincidunt ut laoreet dolore magna aliquam erat volutpat. Ut wisi enim ad minim veniam, quis nostrud exerci tation ullamcorper suscipit lobortis nisl ut aliquip ex ea commodo consequat.</p>
<div class="abs hrule"></div>
<h2 class="abs grow">Grow Your Business</h2>
<ul class="abs features">
  <li><svg width="16" height="16" viewBox="0 0 16 16"><rect x="1" y="1" width="14" height="14" fill="none" stroke="#1d5aa6" stroke-width="2"/><path d="M1 5.7h14M1 10.3h14M5.7 1v14M10.3 1v14" stroke="#1d5aa6" stroke-width="1.5"/></svg>Customised selling platform</li>
  <li><svg width="16" height="16" viewBox="0 0 16 16"><rect x="1" y="2" width="13" height="13" fill="none" stroke="#1d5aa6" stroke-width="1.5"/><path d="M4 13l4-9 4 9M5.5 10h5" fill="none" stroke="#1d5aa6" stroke-width="1.5"/></svg>Unique designs, every time</li>
  <li><svg width="18" height="16" viewBox="0 0 18 16"><circle cx="6" cy="5" r="3" fill="#1d5aa6"/><circle cx="12" cy="5" r="3" fill="#1d5aa6"/><path d="M1 15c0-4 2-6 5-6s5 2 5 6zM8 15c0-4 2-6 4-6s5 2 5 6z" fill="#1d5aa6"/></svg>We focus on your customers</li>
  <li><svg width="18" height="16" viewBox="0 0 18 16"><path d="M1 2h3l2 9h9l2-7H5" fill="none" stroke="#1d5aa6" stroke-width="1.6"/><circle cx="7" cy="14" r="1.5" fill="#1d5aa6"/><circle cx="14" cy="14" r="1.5" fill="#1d5aa6"/></svg>Easy to use order process</li>
  <li><svg width="20" height="16" viewBox="0 0 20 16"><rect x="1" y="2" width="13" height="9" fill="none" stroke="#1d5aa6" stroke-width="2"/><path d="M5 14h5" stroke="#1d5aa6" stroke-width="2"/><rect x="15" y="5" width="4" height="10" fill="#1d5aa6"/></svg>Reliable</li>
</ul>

<footer class="abs footer"></footer>
<p class="abs foot-copy">© 2013 | harborvantage-example.com All rights reserved</p>
<div class="abs foot-line"></div>
<div class="abs social bottom"><span></span><span></span><span></span><span></span></div>

<p class="abs news-title">Newsletter Signup</p>
<div class="abs news-input"><span>Subscribe</span></div>

<p class="abs call-title">Call Us Today</p>
<div class="abs call-icon"><svg width="11" height="11" viewBox="0 0 11 11"><path d="M2 1l2 0 1 3-1.5 1c.6 1.3 1.2 1.9 2.5 2.5L7 6l3 1v2c0 1-1 1.5-2 1.3C5 9.8 1.2 6 .7 3 .5 2 1 1 2 1z" fill="#555"/></svg></div>
<p class="abs phone">0800-2002-200</p>
</body>
</html>
```